Website for Company to help with House Restoration from Hurricane Damage

Crisp, Clean and Professional!

I need a FRONT page for a website. I need it created in photoshop with the layers intact. We DO NOT need the HTML or DRB for the site. Simply the design. Any fonts you use will need to be included if they are not standard. Please make sure any fonts you use in the body of the text are available for use on Google Fonts.

I have attached a word doc that lists the menu items and additional instructions.

A little about the company - after Hurricane Marlow - DRB developed a system which allows the house to be raised, the Tremlets installed, and the house reset on the Tremlets without the expense of moving the house or driving new pilings. This option can be installed in a matter of days with limited space and at a lower construction cost.

Please refer to the attached musthaves.doc and images that are included.

The main page must incorporate the menu, the attached photos w/ text underneath (text is in the word doc attached), and the text included in the word doc.

Standard footer with contact info as well.

If you have questions please contact us!
Updates

Designs are due by Friday! We will pick one this weekend.  We are unable to change it from 10 days to 5.  Thank you!!!

Target Market(s)

People who lost their homes or businesses due to a hurricane.

Industry/Entity Type

Construction

Requirements
Must have
• See attached musthaves.doc

```html
<!DOCTYPE html>
<html lang="en">
<head>
<meta charset="utf-8">
<title>Durable Riser Bracing, LLC</title>
<link href="https://fonts.googleapis.com/css2?family=Quattrocento:wght@400;700&family=Open+Sans:wght@400;700&display=swap" rel="stylesheet">
<style>
:root{
  --olive:#768c52;
  --olive-dark:#5f7440;
  --olive-text:#6b7f4a;
  --sage:#c3d29d;
  --sage-dark:#9fb273;
  --ink:#1a1a1a;
  --grey-text:#7a7a7a;
  --card-bg:#f4f4f4;
  --card-line:#e2e2e2;
  --accent-red:#c0141b;
}
*{box-sizing:border-box;margin:0;padding:0}
html,body{width:1200px;height:1178px;overflow:hidden;background:#fff}
body{font-family:"Quattrocento",serif;color:var(--ink)}
.wrap{width:892px;margin:0 auto;position:relative}
.site-header{height:130px;border-top:4px solid #000;background:linear-gradient(#c6d3a8 0%,#eef2e3 60%,#fff 100%)}
.site-header .wrap{height:126px}
.brand{position:absolute;left:0;top:14px;display:flex;align-items:center;gap:14px}
.brand-mark{width:96px;height:96px;background:var(--olive);border-radius:6px}
.brand-name{font-family:"Quattrocento",serif;font-weight:700;font-size:36px;color:var(--olive-text);margin-top:36px}
.phone{position:absolute;right:0;top:20px;display:flex;align-items:center;gap:6px;font-weight:700;font-size:23px;color:var(--olive-text)}
.main-nav{height:40px;background:var(--olive)}
.main-nav ul{list-style:none;display:flex;height:40px;align-items:center}
.main-nav li{font-size:14px;color:#fff;text-transform:uppercase;letter-spacing:.3px;margin-right:33px}
.main-nav li:last-child{margin-left:6px}
.hero{height:364px;border-top:1px solid #fff;background:linear-gradient(#a9a0b0 0%,#e0a8a0 30%,#f2c49c 42%,#a2909c 55%,#7a6c78 75%,#8e7a78 100%)}
.fade{height:60px;background:linear-gradient(#d9d9d9,#fff)}
.intro{margin-top:-28px}
.intro h1{font-size:21.5px;font-weight:400;margin-bottom:8px}
.intro h1 span{color:var(--olive-text)}
.intro p{font-size:13.2px;line-height:18.1px;text-align:justify;margin-bottom:18px}
.cards{display:flex;justify-content:space-between;margin-top:14px}
.card{position:relative;width:285px;height:199px;background:var(--card-bg);border:1px solid var(--card-line);border-radius:4px;overflow:hidden;text-align:center}
.card h2{height:66px;background:linear-gradient(var(--olive-dark),var(--olive));color:#fff;font-size:18.5px;font-weight:700;line-height:22px;display:flex;align-items:center;justify-content:center;padding:0 8px}
.card p{font-size:13.2px;line-height:21.5px;color:var(--grey-text);padding:10px 14px 0;text-align:center}
.more{position:absolute;left:0;right:0;bottom:14px;display:flex;justify-content:center;align-items:center;gap:5px;font-family:"Open Sans",sans-serif;font-size:9px;font-weight:700;line-height:12px;color:var(--accent-red);letter-spacing:.4px}
.site-footer{margin-top:21px;background:var(--sage);height:124px}
.site-footer .wrap{height:124px}
.contact h3,.social h3{font-size:24px;font-weight:400;padding-top:8px;margin-bottom:6px}
.contact p{font-size:13.5px;line-height:18px}
.social{position:absolute;right:0;top:0}
.social ul{list-style:none;display:flex;gap:4px;margin-top:8px;justify-content:flex-end}
.social li{width:36px;height:39px;background:var(--olive)}
.copyright{height:29px;background:var(--sage-dark);color:#eef2e1;font-family:"Open Sans",sans-serif;font-size:9.5px;text-align:center;line-height:29px;letter-spacing:.4px}
</style>
</head>
<body>
<header class="site-header">
  <div class="wrap">
    <div class="brand">
      <div class="brand-mark"></div>
      <div class="brand-name">Durable Riser Bracing</div>
    </div>
    <div class="phone">
      <svg width="28" height="22" viewBox="0 0 28 22" aria-hidden="true"><path d="M2 8c0-4 6-6 12-6s12 2 12 6l-5 2-2-3H9L7 10z" fill="#555"/><rect x="6" y="11" width="16" height="10" rx="2" fill="#555"/><circle cx="14" cy="16" r="3" fill="#ddd"/></svg>
      (555) 014-2290
    </div>
  </div>
</header>
<nav class="main-nav">
  <ul class="wrap">
    <li>Home</li><li>Services</li><li>About Us</li><li>Product Specifications</li><li>Design Documentation</li><li>Contact Us</li>
  </ul>
</nav>
<div class="hero" role="img" aria-label="Photo of a parent and small child on a beach at sunset, boats on the bay behind them"></div>
<div class="fade"></div>
<main class="wrap intro">
  <h1>Welcome to <span>Durable Riser Bracing, LLC</span></h1>
  <p>Systems for extending the height of existing piles are not available on today’s market. Durable Riser Bracing, LLC (DRB) has developed two systems to allow for Piles to be extended that provide superior structural support without corrosion and maintenance concerns. We provided two systems, a complete system, Pile Cap Extension Tremlets, and Pile Splice. These two systems allow a home to be raised to by up to 54”, higher extensions possible with additional design consideration for lateral support. Shown below is the full Piling Extension system, which connects to the top of the existing pile. The system modular and can be cut to meet specific needs of the home.</p>
  <p>Our Patented Piling system has been designed to withstand the corrosive environment of beach communities. The salt water and windblown sand corrodes unprotected materials, and yes, even stainless steel. Our system utilizes a high strength carbon fiber material that is corrosion proof from salt water and UV proof. The system will not erode, decay or loose strength over time. The system has three installation conditions, for raising a house on existing pilings, repairing damaged pilings, and for connecting new pilings to floor joists in new construction.</p>
  <section class="cards">
    <article class="card">
      <h2>Raising a house on<br>existing pilings</h2>
      <p>Lorem Ipsum. Proin gravida nibh vel velit auctor aliquet. Aenean sollicitudin, lorem quis bibendum auctor, nisi elit consequat ipsum, nec sagittis sem nibh id elit. Duis</p>
      <span class="more">View more <svg width="13" height="11" viewBox="0 0 13 11" aria-hidden="true"><path d="M1 5.5h10M7 1.5l4 4-4 4" stroke="#333" stroke-width="1.6" fill="none"/></svg></span>
    </article>
    <article class="card">
      <h2>Repairing<br>damaged pilings</h2>
      <p>Lorem Ipsum. Proin gravida nibh vel velit auctor aliquet. Aenean sollicitudin, lorem quis bibendum auctor, nisi elit consequat ipsum, nec sagittis sem nibh id elit. Duis</p>
      <span class="more">View more <svg width="13" height="11" viewBox="0 0 13 11" aria-hidden="true"><path d="M1 5.5h10M7 1.5l4 4-4 4" stroke="#333" stroke-width="1.6" fill="none"/></svg></span>
    </article>
    <article class="card">
      <h2>Connecting new pilings to<br>floor joists in new construction</h2>
      <p>Lorem Ipsum. Proin gravida nibh vel velit auctor aliquet. Aenean sollicitudin, lorem quis bibendum auctor, nisi elit consequat ipsum, nec sagittis sem nibh id elit. Duis</p>
      <span class="more">View more <svg width="13" height="11" viewBox="0 0 13 11" aria-hidden="true"><path d="M1 5.5h10M7 1.5l4 4-4 4" stroke="#333" stroke-width="1.6" fill="none"/></svg></span>
    </article>
  </section>
</main>
<footer>
  <div class="site-footer">
    <div class="wrap">
      <div class="contact">
        <h3>Contact info</h3>
        <p>Durable Riser Bracing, LLC</p>
        <p>PO Box 4410, Millbrook Falls, PA 18000-0410</p>
        <p>Tel: (555) 014-2290</p>
        <p>Email: sales@durableriserbracing.com</p>
      </div>
      <div class="social">
        <h3>Lets get social</h3>
        <ul>
          <li aria-label="Social link 1"></li><li aria-label="Social link 2"></li><li aria-label="Social link 3"></li><li aria-label="Social link 4"></li>
        </ul>
      </div>
    </div>
  </div>
  <div class="copyright">Copy © 2013 Durable Riser Bracing, LLC. All rights reserved.</div>
</footer>
</body>
</html>
```